Lotus Haven Beauty & Spa Business Card Design

Hello, I have a Beauty salon On my own Property. It is a Balinese Style Salon with a Spa & Sauna together with all beauty Options available. I have strived myself to get trained In Indonesia as well as here so I can offer my clients something "unique & special" somewhere to unwind as well as be pampered and step out of reality for even a little while.

So with all this in mind I would like to keep everything on the "natural style look" if possible....

I was hoping to have some kind Of Kraft look paper or background look, with a Olive/lime Natural Green colour Logo and Name on the front. "Lotus Haven Beauty & Spa"

Details (im really not sure on how it should be placed on the card whether back or front?)
I'd really like written somewhere on the card, somewhere
.... Lotus Haven Calm ...

also if room maybe a few things that I do eg. Waxing, Tanning, teeth Whitening, all kinds of Beauty and much more.

DETAILS are
Lotus Haven Beauty & Spa
Melissa Tindall
Ph: 04 837 25 614
Address: 9 Kinwood Place
Balmoral NSW 2283

(facebook logo) www.examplebook.test/LotusHavenBeautySpa

I think this is all the info that I need on the card.. if I have forgotten anything or if you need anything else please dont hesitate to contact me....
& just maybe a few dotted lines so I can write appt times etc.. I was also thinking maybe a QR BarCode. Sorry this is the first time I have done any business cards so forgive me I dont really have a clue.

please let me know what else you need me to do from here thanks for your time.
Missy

Industry/Entity Type

Salon

Font styles to use
Script

Colors
acd036
9bcb3c

```html
<!DOCTYPE html>
<html lang="en">
<head>
<meta charset="utf-8">
<title>Lotus Haven Beauty &amp; Spa – Business Card</title>
<link href="https://fonts.googleapis.com/css2?family=Great+Vibes&family=Montserrat:wght@400;600;700&display=swap" rel="stylesheet">
<style>
  :root{
    --bg:#e9e7e3;
    --card:#ffffff;
    --card-shade:#f1f1f1;
    --lime:#acd036;
    --lime-deep:#9bcb3c;
    --ink:#2b2b2b;
    --ink-soft:#555555;
    --white:#ffffff;
  }
  *{box-sizing:border-box;margin:0;padding:0}
  html,body{width:1200px;height:901px;overflow:hidden;background:var(--bg)}
  body{font-family:"Montserrat",Arial,sans-serif;position:relative}
  .card{
    position:absolute;top:302px;width:520px;height:297px;border-radius:26px;
    background:radial-gradient(ellipse at 60% 35%,var(--card) 55%,var(--card-shade) 100%);
    box-shadow:0 10px 30px rgba(0,0,0,.18);overflow:hidden;
  }
  .card--front{left:55px}
  .card--back{left:625px}
  .front-swoosh{position:absolute;inset:0;width:100%;height:100%}
  .holder{position:absolute;left:28px;top:26px;width:200px}
  .holder__name{font-weight:700;font-size:16px;letter-spacing:1.2px;color:var(--ink);text-transform:uppercase;white-space:nowrap}
  .holder__role{font-weight:400;font-size:10.5px;color:var(--ink-soft);margin-top:3px}
  .brand{position:absolute;display:flex;align-items:center;gap:12px}
  .brand__mark{border-radius:50%;background:var(--lime);flex:none}
  .brand__text{display:flex;flex-direction:column}
  .brand__name{font-family:"Great Vibes",cursive;color:var(--lime);line-height:1;white-space:nowrap}
  .brand__tag{font-family:"Great Vibes",cursive;color:var(--lime);line-height:1.3;white-space:nowrap}
  .card--front .brand{right:30px;top:30px}
  .card--front .brand__mark{width:40px;height:40px}
  .card--front .brand__name{font-size:25px}
  .card--front .brand__tag{font-size:14px;padding-left:26px}
  .card--back .brand{left:50%;top:50%;transform:translate(-50%,-50%)}
  .card--back .brand__mark{width:52px;height:52px}
  .card--back .brand__name{font-size:32px}
  .card--back .brand__tag{font-size:16px;padding-left:30px}
  .contact{position:absolute;left:28px;bottom:22px;list-style:none;color:var(--white);font-size:10.5px;font-weight:600}
  .contact li{display:flex;align-items:center;gap:8px;height:18px}
  .contact svg{width:11px;height:11px;flex:none}
  .contact .spacer{width:11px;flex:none}
  .contact .gap{height:8px}
</style>
</head>
<body>

<section class="card card--front" aria-label="Card front">
  <svg class="front-swoosh" viewBox="0 0 520 297" preserveAspectRatio="none" aria-hidden="true">
    <path d="M0 110 C150 128 330 180 520 244 L520 297 L0 297 Z" fill="var(--lime)"/>
    <path d="M0 98 C160 116 340 170 520 230" fill="none" stroke="var(--lime)" stroke-width="2"/>
    <path d="M0 116 C150 134 330 186 520 250" fill="none" stroke="var(--white)" stroke-width="3"/>
  </svg>

  <div class="holder">
    <p class="holder__name">Daniel Whitford</p>
    <p class="holder__role">Managing Director</p>
  </div>

  <div class="brand">
    <span class="brand__mark" aria-hidden="true"></span>
    <div class="brand__text">
      <span class="brand__name">Lotus Haven</span>
      <span class="brand__name">Beauty &amp; Spa</span>
      <span class="brand__tag">Lotus Haven Calm</span>
    </div>
  </div>

  <ul class="contact">
    <li>
      <svg viewBox="0 0 12 12"><path d="M6 1a3.5 3.5 0 0 0-3.5 3.5C2.5 7.5 6 11 6 11s3.5-3.5 3.5-6.5A3.5 3.5 0 0 0 6 1zm0 5a1.4 1.4 0 1 1 0-2.8A1.4 1.4 0 0 1 6 6z" fill="currentColor"/></svg>
      41 Cedar Row
    </li>
    <li><span class="spacer"></span>Brookfield Lane</li>
    <li class="gap"></li>
    <li>
      <svg viewBox="0 0 12 12"><path d="M3 1l2 2.5-1.2 1.2a6 6 0 0 0 3.5 3.5L8.5 7 11 9l-1.3 1.8C5.5 10.5 1.5 6.5 1.2 2.3z" fill="currentColor"/></svg>
      02 5550 1947
    </li>
    <li>
      <svg viewBox="0 0 12 12"><rect x="1" y="2" width="10" height="8" rx="1" fill="none" stroke="currentColor"/><rect x="3" y="4" width="6" height="2" fill="currentColor"/></svg>
      02 5550 1947
    </li>
    <li>
      <svg viewBox="0 0 12 12"><rect x="1" y="2.5" width="10" height="7" fill="none" stroke="currentColor"/><path d="M1 2.5l5 4 5-4" fill="none" stroke="currentColor"/></svg>
      hello@lotushaven.test
    </li>
    <li>
      <svg viewBox="0 0 12 12"><circle cx="6" cy="6" r="5" fill="none" stroke="currentColor"/><path d="M1 6h10M6 1c-2.5 3-2.5 7 0 10M6 1c2.5 3 2.5 7 0 10" fill="none" stroke="currentColor"/></svg>
      www.lotushaven.test
    </li>
  </ul>
</section>

<section class="card card--back" aria-label="Card back">
  <div class="brand">
    <span class="brand__mark" aria-hidden="true"></span>
    <div class="brand__text">
      <span class="brand__name">Lotus Haven</span>
      <span class="brand__name">Beauty &amp; Spa</span>
      <span class="brand__tag">Lotus Haven Calm</span>
    </div>
  </div>
</section>

</body>
</html>
```